Real Estate Entrepreneur needs a business card

I am a real estate entrepreneur, I buy houses for investment purposes, I act as a real estate agent representing buyers and sellers in residential home transactions, I am a contractor that does a wide range of home repairs and construction. I'd like a design that can stick with me through the years as my business grows and morphs to fit any niche I decide to pursue as markets change.

Target Market(s)

Anyone with interest that may be related to real estate.

Industry/Entity Type

Real Estate

Contact Information for Business Card

A card that stands out and doesn't put me in any one box. My business will evolve over time and I need a card that can stay relevant.

Colors

Designer to choose colors to be used in the design.

Requirements
Must have
• Character
Nice to have
• I'm open
Should not have
• Cliche houses and hammers

```html
<!DOCTYPE html>
<html lang="en">
<head>
<meta charset="utf-8">
<title>Reid Calloway — Business Card</title>
<link rel="stylesheet" href="https://fonts.googleapis.com/css2?family=Montserrat:wght@500;800&display=swap">
<style>
  :root {
    --backdrop: #2b2b2d;
    --card: #ecebe8;
    --ink: #2a2a2a;
    --ink-soft: #3a3a3a;
    --gold: #c9b57e;
    --gold-deep: #a8925a;
  }
  * { box-sizing: border-box; margin: 0; padding: 0; }
  html, body { width: 1200px; height: 900px; overflow: hidden; }
  body {
    background: var(--backdrop);
    font-family: "Montserrat", sans-serif;
    display: flex;
    align-items: center;
    justify-content: center;
    gap: 80px;
  }
  .card {
    width: 360px;
    height: 640px;
    background: var(--card);
    border-radius: 34px;
    display: flex;
    flex-direction: column;
    align-items: center;
    box-shadow: 0 18px 40px rgba(0,0,0,0.45);
  }
  .card--front { padding-top: 150px; }
  .card--back { padding-top: 150px; }
  .brand-mark {
    width: 120px;
    height: 120px;
    border-radius: 50%;
    background: linear-gradient(160deg, var(--gold), var(--gold-deep));
    margin-bottom: 34px;
  }
  .brand-name {
    font-weight: 800;
    font-size: 34px;
    letter-spacing: 0.5px;
    color: var(--ink);
    line-height: 1;
    text-transform: uppercase;
    text-align: center;
  }
  .brand-role {
    font-weight: 500;
    font-size: 17px;
    letter-spacing: 1px;
    color: var(--ink-soft);
    margin-top: 8px;
  }
  .divider {
    width: 18px;
    height: 3px;
    background: var(--ink);
    margin: 34px 0 26px;
  }
  .contact-icons { display: flex; gap: 18px; margin-bottom: 30px; }
  .contact-icon {
    width: 26px;
    height: 26px;
    border-radius: 50%;
    background: var(--ink);
    display: flex;
    align-items: center;
    justify-content: center;
  }
  .contact-icon svg { width: 14px; height: 14px; }
  .contact-list { list-style: none; text-align: center; }
  .contact-list li {
    font-weight: 500;
    font-size: 15px;
    color: var(--ink);
    margin-bottom: 16px;
    letter-spacing: 0.3px;
  }
  .divider--end { margin: 4px 0 0; }
</style>
</head>
<body>

  <section class="card card--front" aria-label="Card front">
    <div class="brand-mark"></div>
    <h1 class="brand-name">Reid Calloway</h1>
    <p class="brand-role">Real Estate Agent</p>
    <span class="divider"></span>
    <div class="contact-icons">
      <span class="contact-icon">
        <svg viewBox="0 0 16 16"><path d="M4 2l2.5 3-1.5 1.5c.8 1.8 2.2 3.2 4 4L10.5 9 13.5 11.5 12 14C7 13.5 2.5 9 2 4z" fill="#ecebe8"/></svg>
      </span>
      <span class="contact-icon">
        <svg viewBox="0 0 16 16"><rect x="2" y="4" width="12" height="8" fill="none" stroke="#ecebe8" stroke-width="1.5"/><path d="M2 4l6 5 6-5" fill="none" stroke="#ecebe8" stroke-width="1.5"/></svg>
      </span>
      <span class="contact-icon">
        <svg viewBox="0 0 16 16"><rect x="5" y="2" width="6" height="7" rx="3" fill="none" stroke="#ecebe8" stroke-width="1.5"/><rect x="5" y="7" width="6" height="7" rx="3" fill="none" stroke="#ecebe8" stroke-width="1.5"/></svg>
      </span>
    </div>
    <ul class="contact-list">
      <li>042-555-0148</li>
      <li>contact@reidcalloway.com</li>
      <li>www.reidcalloway.com</li>
    </ul>
    <span class="divider divider--end"></span>
  </section>

  <section class="card card--back" aria-label="Card back">
    <div class="brand-mark"></div>
    <h2 class="brand-name">Reid Calloway</h2>
    <p class="brand-role">Real Estate Agent</p>
  </section>

</body>
</html>
```